Business Card design for construction company

I would like a business card design for a construction company - ORD Builders. I have attached the ai logo file for use. I would like the card to be very smart and clean and incorporate only white and the two colours in the logo. I would like the card to have two sides. One side can just have the logo, the other with the relevant information.

Target Market(s)

Building and Construction Clients

Industry/Entity Type

Business

Contact Information for Business Card

Name: Tom Harcliffe
Company: ORD Builders Pty Limited
Address: 14 Mulberry Crescent Oakvale Heights 2093
Phone: 0432 517 208
Email: tomh@ordbuilders.example.au

Font styles to use
Serif
Sans Serif

Requirements
Must have
• Details noted above
• Logo as provided
• Colours as in logo
• Square edges
• A font that compliments the logo
Should not have
• Any colour other than white and those in logo
• Rounded edges

```html
<!DOCTYPE html>
<html lang="en">
<head>
<meta charset="utf-8">
<title>ORD Builders – Business Card</title>
<link href="https://fonts.googleapis.com/css2?family=Open+Sans:wght@400;600;700&display=swap" rel="stylesheet">
<style>
  :root {
    --bg: #9a9a9a;
    --card-dark: #5e5f61;
    --card-light: #ffffff;
    --ink: #3c3d3f;
    --ink-soft: #555658;
    --accent: #1a8ad4;
    --rule: #a7a8aa;
    --brand-light: #e9e9ea;
  }
  * { margin: 0; padding: 0; box-sizing: border-box; }
  html, body { width: 1200px; height: 900px; overflow: hidden; }
  body {
    background: var(--bg);
    font-family: "Open Sans", Arial, sans-serif;
    position: relative;
  }
  .card {
    position: absolute;
    width: 620px;
    height: 354px;
    border-radius: 0;
    box-shadow: 0 6px 14px rgba(0,0,0,0.25);
  }
  .card--back {
    left: 80px; top: 60px;
    background: var(--card-dark);
    display: flex; align-items: center; justify-content: center;
  }
  .card--front {
    left: 500px; top: 486px;
    background: var(--card-light);
  }
  .brand {
    font-weight: 600;
    letter-spacing: 0.12em;
    text-transform: uppercase;
    white-space: nowrap;
  }
  .card--back .brand { color: var(--brand-light); font-size: 40px; }
  .card--front .brand {
    position: absolute; left: 48px; top: 62px;
    color: var(--ink); font-size: 30px;
  }
  .office {
    position: absolute; right: 40px; top: 168px;
    text-align: right; color: var(--ink-soft);
    font-style: normal; font-size: 13px; line-height: 1.5;
    white-space: nowrap;
  }
  .office__name { color: var(--ink); font-weight: 600; }
  .holder {
    position: absolute; left: 120px; top: 216px;
    color: var(--accent); font-weight: 700; font-size: 30px;
    line-height: 40px; letter-spacing: -0.01em; white-space: nowrap;
  }
  .divider {
    position: absolute; left: 120px; right: 40px; top: 262px;
    height: 1px; background: var(--rule);
  }
  .contacts {
    position: absolute; left: 120px; top: 274px;
    list-style: none; color: var(--ink-soft); font-size: 13.5px; line-height: 1.55;
  }
  .contacts li { display: flex; align-items: center; gap: 8px; white-space: nowrap; }
  .contacts svg { width: 13px; height: 13px; fill: var(--accent); flex: none; }
</style>
</head>
<body>
  <section class="card card--back" aria-label="Card back">
    <span class="brand">ORD Builders</span>
  </section>

  <section class="card card--front" aria-label="Card front">
    <span class="brand">ORD Builders</span>

    <address class="office">
      <span class="office__name">ORD Builders Pty Limited</span><br>
      14 Mulberry Crescent<br>
      Oakvale Heights 2093
    </address>

    <h1 class="holder">Tom Harcliffe</h1>
    <div class="divider"></div>

    <ul class="contacts">
      <li>
        <svg viewBox="0 0 16 16" aria-hidden="true"><path d="M3.6 1.2l2.2 2.6c.3.4.3.9 0 1.2L4.6 6.3c.9 2 2.6 3.7 4.6 4.6l1.3-1.2c.3-.3.8-.3 1.2 0l2.6 2.2c.4.3.4.9.1 1.2l-1.3 1.4c-.5.5-1.2.7-1.9.5C6.3 13.6 2.4 9.7 1 4.7c-.2-.7 0-1.4.5-1.9L2.4 1.1c.4-.3.9-.3 1.2.1z"/></svg>
        0432 517 208
      </li>
      <li>
        <svg viewBox="0 0 16 16" aria-hidden="true"><path d="M1 3h14v1.2L8 8.6 1 4.2z"/><path d="M1 5.6l7 4.4 7-4.4V13H1z"/></svg>
        tomh@ordbuilders.example.au
      </li>
      <li>
        <svg viewBox="0 0 16 16" aria-hidden="true"><path d="M8 1a7 7 0 100 14A7 7 0 008 1zm5.4 6.3h-2.3a11 11 0 00-.8-4 5.6 5.6 0 013.1 4zM8 2.5c.7.9 1.4 2.6 1.6 4.8H6.4C6.6 5.1 7.3 3.4 8 2.5zM5.7 3.3a11 11 0 00-.8 4H2.6a5.6 5.6 0 013.1-4zM2.6 8.7h2.3c.1 1.5.4 2.9.8 4a5.6 5.6 0 01-3.1-4zM8 13.5c-.7-.9-1.4-2.6-1.6-4.8h3.2c-.2 2.2-.9 3.9-1.6 4.8zm2.3-.8c.4-1.1.7-2.5.8-4h2.3a5.6 5.6 0 01-3.1 4z"/></svg>
        www.ordbuilders.example.au
      </li>
    </ul>
  </section>
</body>
</html>
```